Korvex Systems*

Stationary design including business cards, letter heads, envelops and email signatures using our new logo

Target Market(s)

Innovative Technologies

Industry/Entity Type

Defense Contracting

Font styles to use
Sans Serif

```html
<!DOCTYPE html>
<html lang="en">
<head>
<meta charset="UTF-8">
<title>Korvex Systems — Business Card</title>
<link href="https://fonts.googleapis.com/css2?family=Open+Sans:wght@400;600;700&display=swap" rel="stylesheet">
<style>
  :root {
    --page-bg: #ececec;
    --card-white: #f4f4f4;
    --card-dark: #2e2e2e;
    --ink: #2a2a2a;
    --ink-soft: #5a5a5a;
    --rule: #8a8a8a;
    --line-light: #ffffff;
  }
  * { box-sizing: border-box; margin: 0; padding: 0; }
  html, body {
    width: 1200px; height: 967px; overflow: hidden;
    background: var(--page-bg);
    font-family: "Open Sans", sans-serif;
  }
  .stage {
    position: relative; width: 1200px; height: 967px;
    display: flex; align-items: center; justify-content: center; gap: 44px;
  }
  .card {
    position: relative; width: 540px; height: 309px;
    box-shadow: 0 6px 18px rgba(0,0,0,0.12);
    overflow: hidden;
  }
  .card-front { background: var(--card-white); color: var(--ink); }
  .card-back { background: var(--card-dark); display: flex; align-items: center; justify-content: center; }

  .brand {
    position: absolute; left: 34px; top: 100px; width: 215px;
    display: flex; align-items: center; gap: 12px;
  }
  .brand-square { width: 26px; height: 26px; border: 2px solid var(--ink); flex: none; }
  .brand-name { font-size: 22px; font-weight: 700; letter-spacing: 0.5px; color: var(--ink); white-space: nowrap; }

  .divider { position: absolute; left: 262px; top: 34px; width: 1px; height: 200px; background: var(--rule); }

  .contact { position: absolute; left: 288px; top: 38px; width: 240px; }
  .person-name { font-size: 21px; font-weight: 700; line-height: 1.1; }
  .person-title { font-size: 13px; color: var(--ink-soft); margin-bottom: 12px; }
  .address { font-size: 13px; line-height: 1.35; color: var(--ink-soft); margin-bottom: 8px; }
  .contact-row { display: flex; align-items: center; gap: 9px; font-size: 13px; color: var(--ink-soft); line-height: 1.55; }
  .contact-row svg { width: 15px; height: 15px; flex: none; }

  .bottom-band { position: absolute; left: 0; right: 0; bottom: 0; height: 10px; background: var(--card-dark); }
  .corner-square { position: absolute; right: 62px; bottom: 10px; width: 34px; height: 34px; border: 2px solid var(--ink); border-bottom: none; background: var(--card-white); }

  .back-square { width: 58px; height: 58px; border: 2px solid var(--line-light); }
</style>
</head>
<body>
<main class="stage">
  <section class="card card-front" aria-label="Business card front">
    <div class="brand">
      <span class="brand-square"></span>
      <span class="brand-name">Korvex Systems</span>
    </div>
    <div class="divider"></div>
    <div class="contact">
      <p class="person-name">Daniel Marsh</p>
      <p class="person-title">CEO</p>
      <p class="address">48 Harlow Park Rd., Unit 7, Westbrook Commons, Alder County</p>
      <p class="contact-row">
        <svg viewBox="0 0 16 16" fill="none" stroke="currentColor" stroke-width="1.4"><circle cx="8" cy="8" r="7"/><path d="M5.5 4.5l1.3 1.6-.8 1c.6 1.2 1.4 2 2.6 2.6l1-.8 1.6 1.3-.8 1.2c-2.8-.4-5-2.6-5.4-5.4z" fill="currentColor" stroke="none"/></svg>
        +1 555 0142 870
      </p>
      <p class="contact-row">
        <svg viewBox="0 0 16 16" fill="none" stroke="currentColor" stroke-width="1.4"><rect x="1" y="3.5" width="14" height="9"/><path d="M1 3.5l7 5.5 7-5.5"/></svg>
        info@korvexsystems.com
      </p>
      <p class="contact-row">
        <svg viewBox="0 0 16 16" fill="none" stroke="currentColor" stroke-width="1.2"><circle cx="8" cy="8" r="7"/><ellipse cx="8" cy="8" rx="3" ry="7"/><path d="M1 8h14M2.2 4.5h11.6M2.2 11.5h11.6"/></svg>
        www.korvexsystems.com
      </p>
    </div>
    <div class="corner-square"></div>
    <div class="bottom-band"></div>
  </section>

  <section class="card card-back" aria-label="Business card back">
    <span class="back-square"></span>
  </section>
</main>
</body>
</html>
```